Agricultural Consulting Website

Provide a modern yet business like website for my new Agriculture Consulting Business in Australia called FenTrove. Whilst we are based in Australia we are targetting both domestic and international markets (especially in Asia). We are targetting corporate, small business, government and farmer clients. The design should compliment our logo also sourced through pixel guild. The webiste should be easy for me to keep updated on a regular basis without the need to go back to the designer.

Industry/Entity Type

Business

Requirements
Must have
• clean crisp feel
• be modern yet business like
• be able to be updated by myself easily

```html
<!DOCTYPE html>
<html lang="en">
<head>
<meta charset="utf-8">
<title>FenTrove – Agricultural Consulting</title>
<link href="https://fonts.googleapis.com/css2?family=Roboto:wght@300;400;500;700&display=swap" rel="stylesheet">
<style>
:root{
  --brown:#6a3106;
  --green:#5a9e10;
  --green-light:#84c11f;
  --green-dark:#5f9a0b;
  --text:#6d6d6d;
  --line:#dcdcdc;
  --white:#ffffff;
}
*{margin:0;padding:0;box-sizing:border-box}
html,body{width:1108px;height:1200px;overflow:hidden}
body{
  position:relative;
  font-family:'Roboto',Arial,sans-serif;
  background:linear-gradient(to bottom,#ffffff 0,#f0f0f0 414px,#eefad8 414px,#f6fdea 700px,#ffffff 1068px);
  color:var(--text);
}
a{text-decoration:none}
.top-bar{position:absolute;left:0;top:0;width:1108px;height:5px;background:var(--brown)}
.page{position:absolute;left:111px;top:5px;width:886px;height:1063px;background:var(--white);box-shadow:0 0 6px rgba(0,0,0,.18)}
.abs{position:absolute}

.brand{left:120px;top:25px;display:flex;align-items:center;gap:10px}
.brand-mark{width:70px;height:70px;background:var(--brown)}
.brand-name{font-size:44px;font-weight:400;color:var(--green);letter-spacing:.5px}

.account{right:121px;top:16px;font-size:13.5px;color:#777}
.account a{color:#888}
.account .sep{margin:0 6px;color:#aaa}
.account .register{color:var(--brown)}

.search{left:766px;top:52px;width:221px;height:31px;display:flex;border:1px solid #d6d6d6;background:#f4f4f4}
.search span{flex:1;font-size:12px;font-style:italic;color:#a0a0a0;padding:8px 0 0 10px}
.search .search-btn{width:34px;height:31px;margin:-1px -1px 0 0;background:var(--brown);display:flex;align-items:center;justify-content:center}

.nav{left:120px;top:106px;width:868px;height:51px;background:linear-gradient(to bottom,var(--green-light),var(--green-dark));display:flex;justify-content:space-between;align-items:center;padding:0 20px}
.nav a{color:var(--white);font-size:14px;letter-spacing:.3px}

.hero{left:120px;top:163px;width:868px;height:353px;border:1px solid var(--line);background:var(--white);padding:3px}
.hero-photo{width:100%;height:100%;background:radial-gradient(ellipse at 55% 40%,#c9e57a 0,#9cc93a 40%,#6c9a20 75%,#4f7a18 100%)}
.hero-caption{left:379px;top:294px;width:351px;height:94px;background:rgba(40,40,40,.72);color:var(--white);font-size:26px;line-height:24px;padding-top:10px}
.hero-caption .l1{padding-left:106px;font-weight:300}
.hero-caption .l2{padding-left:52px;font-weight:300}
.hero-caption b{font-weight:700}
.hero-caption .l3{padding-left:115px;font-weight:700}
.dots{left:518px;top:480px;display:flex;gap:5px}
.dots i{width:14px;height:14px;border-radius:50%;background:var(--white)}
.dots i.active{background:var(--brown)}

.service{top:538px;width:262px;height:260px}
.service .photo{width:262px;height:126px}
.service h3{margin-top:6px;font-size:17px;font-weight:400;color:var(--brown);letter-spacing:.3px}
.service p{margin-top:1px;font-size:12.5px;line-height:18.5px;color:var(--text);letter-spacing:.2px}
.btn{display:inline-block;width:74px;height:29px;background:var(--green-light);color:var(--white);font-size:12.5px;font-weight:500;text-align:center;line-height:29px;letter-spacing:.5px}
.service .btn{position:absolute;top:224px;left:0}

.panel{top:817px;height:236px;background:linear-gradient(to bottom,#f1f1f1,#ffffff 90%)}
.welcome{left:120px;width:572px;padding:19px 11px 0 11px}
.welcome .photo{float:left;width:150px;height:126px;margin:0 17px 2px 0;background:linear-gradient(to bottom,#6f9a3c 0,#8aa85a 22%,#c6a27b 35%,#b88f68 100%)}
.panel h2{font-size:22px;font-weight:400;color:var(--green);letter-spacing:.4px;margin-bottom:6px}
.welcome p{font-size:12.5px;line-height:21.2px;color:var(--text);letter-spacing:.25px;white-space:nowrap}
.welcome p .below{display:block;line-height:19px;margin-top:2px}
.welcome .btn{position:absolute;left:9px;top:205px}
.news{left:711px;width:277px;padding:19px 19px 0 19px}
.news .date{font-size:12px;font-weight:500;color:var(--brown);letter-spacing:.3px}
.news p{margin-top:2px;font-size:12px;line-height:18.5px;color:var(--text);letter-spacing:.2px;white-space:nowrap}
.news .btn{position:absolute;left:19px;top:205px}

.footer{left:0;top:1068px;width:1108px;height:132px;background:var(--brown)}
.footer-brand{left:120px;top:1101px;display:flex;align-items:center;gap:8px}
.footer-brand .brand-mark{width:42px;height:42px;background:#f2f2f2}
.footer-brand .brand-name{font-size:29px;color:var(--white)}
.copyright{left:121px;top:1155px;font-size:13px;color:#7fb32a;letter-spacing:.3px}
.connect{left:849px;top:1089px;font-size:14.5px;color:var(--white);letter-spacing:.3px}
.social{left:850px;top:1118px;display:flex;gap:8px}
.social i{width:28px;height:28px;border-radius:4px;background:#c9c9c9}
</style>
</head>
<body>
<div class="top-bar"></div>
<div class="page"></div>

<div class="abs brand">
  <div class="brand-mark"></div>
  <div class="brand-name">FenTrove</div>
</div>

<div class="abs account"><a href="#">Log in</a><span class="sep">|</span><a href="#" class="register">Register</a></div>

<div class="abs search">
  <span>Search...</span>
  <div class="search-btn">
    <svg width="20" height="20" viewBox="0 0 20 20"><circle cx="12" cy="8" r="5" fill="none" stroke="#fff" stroke-width="2.2"/><line x1="8.5" y1="11.5" x2="3" y2="17" stroke="#fff" stroke-width="3" stroke-linecap="round"/></svg>
  </div>
</div>

<nav class="abs nav">
  <a href="#">Home</a><a href="#">About Us</a><a href="#">Our Services</a><a href="#">Projects</a><a href="#">News &amp; Events</a><a href="#">Gallery</a><a href="#">Blog</a><a href="#">Contact Us</a>
</nav>

<div class="abs hero"><div class="hero-photo" role="img" aria-label="Close-up of young green maize plants in a field"></div></div>
<div class="abs hero-caption">
  <div class="l1"><b>WE</b> CARE</div>
  <div class="l2">ABOUT <b>YOUR</b></div>
  <div class="l3">AGRICULTURE</div>
</div>
<div class="abs dots"><i class="active"></i><i></i><i></i><i></i></div>

<section class="abs service" style="left:120px">
  <div class="photo" role="img" aria-label="Worker tending seedling trays in a greenhouse nursery" style="background:linear-gradient(to bottom,#9aa48e,#5f7a45 55%,#3f5a2c)"></div>
  <h3>Small Business</h3>
  <p>Aliquam molestie, mi et imperdiet euismod, dui purus auctor tellus, et interdum lacus lectus et ante. ..</p>
  <a class="btn" href="#">MORE</a>
</section>
<section class="abs service" style="left:423px">
  <div class="photo" role="img" aria-label="Community meeting held outdoors under trees" style="background:linear-gradient(to bottom,#3f5a2e,#6b6a55 50%,#8a7f70)"></div>
  <h3>Government</h3>
  <p>Aliquam molestie, mi et imperdiet euismod, dui purus auctor tellus, et interdum lacus lectus et ante. ..</p>
  <a class="btn" href="#">MORE</a>
</section>
<section class="abs service" style="left:726px">
  <div class="photo" role="img" aria-label="Consultants taking notes beside a tractor in a green field" style="background:linear-gradient(to right,#8a3a30,#6b8a45 45%,#5a8a32)"></div>
  <h3>Farmer Clients</h3>
  <p>Aliquam molestie, mi et imperdiet euismod, dui purus auctor tellus, et interdum lacus lectus et ante. ..</p>
  <a class="btn" href="#">MORE</a>
</section>

<section class="abs panel welcome">
  <div class="photo" role="img" aria-label="Cupped hands holding soil with a young seedling"></div>
  <h2>Welcome to Our Site</h2>
  <p>Aliquam molestie, mi et imperdiet euismod, dui purus auctor tellus,<br>et interdum lacus lectus et ante. Sed accumsan sollicitudin<br>sapien, sit amet adipiscing turpis gravida ac. In congue, neque ac<br>lobortis volutpat, libero mauris varius mi, vitae suscipit ipsum<br>ligula vitae risus. Duis aliquam nibh a dui iaculis viverra id a velit.<span class="below">Vivamus egestas risus in magna varius commodo. Sed semper viverra egestas. Etiam pretium<br>porttitor lectus, vel ornare neque porta volutpat.</span></p>
  <a class="btn" href="#">MORE</a>
</section>

<section class="abs panel news">
  <h2>News &amp; Events</h2>
  <div class="date">NOVEMBER 21, 2013</div>
  <p>Aliquam molestie, mi et imperdiet euis-<br>mod, dui purus auctor tellus, et interdum<br>lacus lectus et ante. Sed accumsan sol-<br>licitudin sapien, sit amet adipiscing turpis<br>gravida ac. In congue, neque ac lobortis<br>volutpat, libero mauris varius mi, vitae<br>suscipit ipsum ligula vitae risus. ...</p>
  <a class="btn" href="#">MORE</a>
</section>

<footer class="abs footer"></footer>
<div class="abs footer-brand">
  <div class="brand-mark"></div>
  <div class="brand-name">FenTrove</div>
</div>
<div class="abs copyright">Copyright ©2013 All Rights Reserved.</div>
<div class="abs connect">Connect Us</div>
<div class="abs social">
  <i role="img" aria-label="Social network link"></i>
  <i role="img" aria-label="Social network link"></i>
  <i role="img" aria-label="Professional network link"></i>
  <i role="img" aria-label="News feed link"></i>
</div>
</body>
</html>
```